Notepads for Marketing pieces-BOLD design

Looking for notepads for marketing pieces with logo, phone number, and website. Maybe something faded in background. Looking for bold and different

```html
<!DOCTYPE html>
<html lang="en">
<head>
<meta charset="utf-8">
<title>Arlen Care Notepad</title>
<link rel="stylesheet" href="https://fonts.googleapis.com/css2?family=Montserrat:wght@700;800&family=Open+Sans:wght@400;600&display=swap">
<style>
  :root {
    --backdrop: #e6e6e6;
    --sheet: #f5f5f5;
    --brand-red: #e0161b;
    --ink: #1c1c1c;
    --ink-soft: #4a4a4a;
    --rule-heavy: #2a2f45;
    --rule-light: #b9bcc2;
  }
  html, body {
    margin: 0;
    padding: 0;
    width: 1200px;
    height: 960px;
    overflow: hidden;
    background: var(--backdrop);
  }
  .notepad-sheet {
    position: absolute;
    left: 300px;
    top: 50px;
    width: 600px;
    height: 860px;
    background: var(--sheet);
    box-shadow: 0 2px 10px rgba(0,0,0,0.08);
    font-family: "Open Sans", sans-serif;
    color: var(--ink);
  }
  .brand-name {
    position: absolute;
    left: 47px;
    top: 74px;
    display: flex;
    align-items: center;
    gap: 8px;
    margin: 0;
    font-family: "Montserrat", sans-serif;
    font-weight: 800;
    font-size: 28px;
    letter-spacing: 1px;
    color: var(--brand-red);
    line-height: 1;
    white-space: nowrap;
  }
  .brand-square {
    width: 22px;
    height: 22px;
    background: var(--brand-red);
  }
  .service-line {
    position: absolute;
    left: 33px;
    top: 128px;
    margin: 0;
    font-family: "Montserrat", sans-serif;
    font-weight: 700;
    font-size: 10px;
    color: var(--ink);
    white-space: nowrap;
  }
  .contact-block {
    position: absolute;
    left: 300px;
    top: 35px;
    width: 270px;
    text-align: center;
    font-style: normal;
    font-size: 12.5px;
    line-height: 20px;
    color: var(--ink-soft);
  }
  .contact-block p { margin: 0; white-space: nowrap; }
  .contact-office { font-weight: 600; color: var(--ink); }
  .contact-address { margin-bottom: 16px !important; }
  .contact-label { color: var(--brand-red); }
  .header-rule {
    position: absolute;
    left: 33px;
    top: 206px;
    width: 534px;
    height: 2px;
    border-top: 2px solid var(--rule-heavy);
    border-bottom: 2px solid var(--rule-heavy);
  }
  .writing-lines {
    position: absolute;
    left: 33px;
    top: 259px;
    width: 534px;
    margin: 0;
    padding: 0;
    list-style: none;
  }
  .writing-lines li {
    height: 44.5px;
    border-top: 1px solid var(--rule-light);
    box-sizing: border-box;
  }
  .site-address {
    position: absolute;
    left: 0;
    right: 0;
    top: 812px;
    margin: 0;
    text-align: center;
    font-size: 13px;
    letter-spacing: 1.5px;
    color: var(--ink-soft);
  }
  .footer-tab {
    position: absolute;
    left: 190px;
    bottom: 0;
    width: 216px;
    height: 12px;
  }
</style>
</head>
<body>
  <main class="notepad-sheet">
    <h1 class="brand-name"><span class="brand-square"></span>ARLEN CARE</h1>
    <p class="service-line">Home Health | Medical Staffing | Outpatient Therapy</p>

    <address class="contact-block">
      <p class="contact-office">Arlen Care Fairview</p>
      <p class="contact-address">4820 Linden Park Road Fairview, OH 40912</p>
      <p><span class="contact-label">tel</span> 555.210.4836</p>
      <p><span class="contact-label">fax</span> 555.310.7729</p>
      <p>office@arlencare.org</p>
    </address>

    <div class="header-rule"></div>

    <ul class="writing-lines">
      <li></li><li></li><li></li><li></li><li></li><li></li>
      <li></li><li></li><li></li><li></li><li></li><li></li>
    </ul>

    <p class="site-address">www.arlencare.org</p>

    <svg class="footer-tab" viewBox="0 0 216 12" preserveAspectRatio="none" aria-hidden="true">
      <polygon points="6,0 210,0 216,12 0,12" fill="var(--brand-red)"/>
    </svg>
  </main>
</body>
</html>
```